New Toothpaste brand needs a logo & packaging design

Our company is launching a new toothpaste and is looking for a logo and packaging design. The toothpaste brand is called Brivana. The packaging should have the same design quality as the major international brands, such as Lumora, Lumora Totalcare, Dentiva, Pexolo, Wind-rise, Marvest, etc. The dominant colors for our brand should be hues of blue, similar to other major brands. In addition, there should be a little bit of green to represent the "Fresh Mint Blast" flavor and the "Extracts of Aloe Vera" included in the ingredients.

There are typically 3 unique sides on a toothpaste box:

The face: Repeated on ~3 sides of the 4 faces of the box
The back: The 4th box face has the instructions for use, ingredients, company information, bar code/product info, and some branding elements.
The sides: Usually consisting of just the logo, flavor etc.

Please refer to existing brands such as Lumora, Lumora Total-care, and Dentiva for an example of typical box layout and elements.

Task Details:
Package Dimensions: 180 mm x 48 mm x 28 mm, 100 ml toothpaste tube
Brand Name: Brivana
Description: Fluoride Toothpaste
Flavor: Fresh Mint Blast
5 Actions: Protects against cavities and tartar, freshens breath, whitens teeth, and maintains healthy gums. These actions can also be made into a list like Lumora Total Care or Dentiva Max care. For instance, Strong Teeth, Fresh Breath, Whitening, Healthy Gums, Cavity and Tartar Protection.
Also contains whitening micro particles and extracts of aloe vera which may be highlighted on the package

Overall, the look should be high quality and with the same look and feel as the big brands mentioned previously. We do not have an existing logo for this brand. The face of the package is the most important element as it is often repeated on several sides and on the tube itself.

Please let me know if you have any questions.

I've attached some of our favorite big brand designs below. I would say the Lumora Total Care and Gleam vers

The logos I've seen so far for Brivana, have been a bit too bold. A little bold is okay, but just needs to be moderate. 

I would like the colors to be bright and appealing. I mentioned shades of blue being the major color, but green should also be highlighted as well, perhaps in a 80% blue to 20% green ratio. 

Target Market(s)

adult consumer of toothpaste, both female and male.

Industry/Entity Type

It Company

Requirements
Must have
• A logo with the brand name: Brivana
Description or sub text: Fluoride Toothpaste
Flavor: Fresh Mint Blast
A phrase or list describing the Toothpaste Actions: e.g., Protects against cavities and tartar, freshens breath, whitens teeth, and maintains healthy gums. Or as a list simialr to Lumora Total Care or Dentiva Max Care:
-Anti-cavity
-Anti-tartar
-Fresh breath
-Whitening
-Healthy Gums

Special ingredient of "whitening micro particles: and "extracts of aloe vera", which should also be highlighted.

The color should mostly be shades of blue, with only a little bit of green to accentuate the fresh mint blast flavor and aloe vera

Nice to have
• The design should really look good next to lumora total care, gleam pure, and dentiva max care. These are our favorite designs.
Should not have
• For aloe vera, there is no need to show the plant.

The Brivana logo shouldn't be too Bold. This should be appeal to all consumers, not just men.

```html
<!DOCTYPE html>
<html lang="en">
<head>
<meta charset="utf-8">
<title>Brivana Toothpaste Carton Dieline</title>
<link rel="stylesheet" href="https://fonts.googleapis.com/css2?family=Open+Sans:ital,wght@0,400;0,600;0,700;0,800;1,600;1,700;1,800&display=swap">
<style>
  :root {
    --sky-deep: #2fa3e0;
    --sky-mid: #6cc3ee;
    --sky-light: #aee0f8;
    --sky-pale: #d4f0fc;
    --mint-stripe: #3cb54a;
    --mint-light: #74c043;
    --mint-deep: #1c8a3c;
    --brand-teal: #157a5c;
    --navy: #2b2f8f;
    --accent-red: #c8202f;
    --badge-yellow: #ffe600;
    --white: #ffffff;
    --dieline: #3a3a3a;
  }
  html, body {
    margin: 0;
    padding: 0;
    width: 1200px;
    height: 774px;
    overflow: hidden;
    background: var(--white);
  }
  .dieline { display: block; width: 1200px; height: 774px; }
  .cut-line { fill: var(--white); stroke: var(--dieline); stroke-width: 1; }
  .panel-edge { stroke: var(--dieline); stroke-width: 0.8; fill: none; }
  .glue-stripe { fill: var(--mint-stripe); }
  .brand-word { font-family: "Open Sans", sans-serif; font-weight: 800; fill: var(--brand-teal); }
  .descriptor { font-family: "Open Sans", sans-serif; font-style: italic; font-weight: 700; fill: var(--navy); }
  .formula-title { font-family: "Open Sans", sans-serif; font-weight: 800; fill: var(--navy); }
  .benefit { font-family: "Open Sans", sans-serif; font-style: italic; font-weight: 700; fill: var(--navy); }
  .benefit-dot { fill: var(--accent-red); }
  .badge-ring { fill: var(--white); stroke: var(--mint-light); stroke-width: 3; }
  .badge-number { font-family: "Open Sans", sans-serif; font-weight: 800; fill: var(--accent-red); }
  .ingredients { font-family: "Open Sans", sans-serif; font-style: italic; font-weight: 600; fill: var(--white); }
  .ingredients-highlight { fill: var(--navy); }
  .volume { font-family: "Open Sans", sans-serif; font-style: italic; font-weight: 700; fill: var(--white); }
  .new-corner { fill: var(--accent-red); }
  .new-label { font-family: "Open Sans", sans-serif; font-weight: 800; fill: var(--badge-yellow); }
  .flavor-top { font-family: "Open Sans", sans-serif; font-weight: 800; fill: var(--mint-light); }
  .flavor-bottom { font-family: "Open Sans", sans-serif; font-style: italic; font-weight: 800; fill: var(--mint-deep); }
</style>
</head>
<body>
<svg class="dieline" viewBox="0 0 1365 880" xmlns="http://www.w3.org/2000/svg" aria-label="Brivana toothpaste carton dieline">
  <defs>
    <linearGradient id="top-panel-fill" x1="0" x2="1" y1="0" y2="0">
      <stop offset="0" stop-color="var(--sky-deep)"/>
      <stop offset="1" stop-color="var(--sky-light)"/>
    </linearGradient>
    <linearGradient id="top-side-fill" x1="0" x2="1" y1="0" y2="0">
      <stop offset="0" stop-color="var(--sky-light)"/>
      <stop offset="1" stop-color="var(--sky-deep)"/>
    </linearGradient>
    <linearGradient id="face-fill" x1="0" x2="1" y1="0" y2="0">
      <stop offset="0" stop-color="var(--sky-mid)"/>
      <stop offset="1" stop-color="var(--sky-light)"/>
    </linearGradient>
    <radialGradient id="logo-glow" cx="0.5" cy="0.5" r="0.5">
      <stop offset="0" stop-color="var(--white)" stop-opacity="0.85"/>
      <stop offset="1" stop-color="var(--white)" stop-opacity="0"/>
    </radialGradient>
    <radialGradient id="mint-burst" cx="0.5" cy="0.55" r="0.65">
      <stop offset="0" stop-color="var(--white)"/>
      <stop offset="0.45" stop-color="var(--sky-pale)"/>
      <stop offset="0.8" stop-color="#9fd6a0"/>
      <stop offset="1" stop-color="var(--sky-deep)"/>
    </radialGradient>
    <radialGradient id="flap-fill" cx="0.5" cy="0.5" r="0.6">
      <stop offset="0" stop-color="var(--sky-pale)"/>
      <stop offset="0.7" stop-color="var(--sky-light)"/>
      <stop offset="1" stop-color="#a6dcc0"/>
    </radialGradient>

    <g id="front-face">
      <rect x="230" y="185" width="655" height="243" fill="url(#face-fill)"/>
      <ellipse cx="430" cy="285" rx="190" ry="110" fill="url(#logo-glow)" role="img" aria-label="Sparkle burst behind the brand name"/>
      <polygon class="new-corner" points="230,185 298,185 230,252"/>
      <text class="new-label" x="259" y="222" font-size="17" text-anchor="middle" transform="rotate(-42 259 222)">NEW</text>
      <text class="brand-word" x="305" y="310" font-size="56" textLength="252" lengthAdjust="spacingAndGlyphs">BRIVANA</text>
      <text class="descriptor" x="405" y="331" font-size="14">Fluoride Toothpaste</text>
      <circle class="badge-ring" cx="606" cy="228" r="24"/>
      <text class="badge-number" x="606" y="242" font-size="38" text-anchor="middle">5</text>
      <text class="formula-title" x="641" y="250" font-size="20">ACTION FORMULA</text>
      <g class="benefit-list">
        <circle class="benefit-dot" cx="596" cy="277" r="2.4"/>
        <text class="benefit" x="601" y="282" font-size="15">Protects Against Cavities and Tartar</text>
        <circle class="benefit-dot" cx="596" cy="295" r="2.4"/>
        <text class="benefit" x="601" y="300" font-size="15">Freshens Breath</text>
        <circle class="benefit-dot" cx="596" cy="312" r="2.4"/>
        <text class="benefit" x="601" y="317" font-size="15">Whitens Teeth</text>
        <circle class="benefit-dot" cx="596" cy="330" r="2.4"/>
        <text class="benefit" x="601" y="335" font-size="15">Maintains Healthy Gums</text>
      </g>
      <rect class="ingredients-highlight" x="486" y="380" width="176" height="15" rx="2"/>
      <text class="ingredients" x="432" y="391" font-size="11">Contains <tspan>WHITENING MICRO PARTICLES</tspan> and Aloe Vera Extracts</text>
      <text class="volume" x="240" y="412" font-size="14">100 ml</text>
    </g>

    <g id="flavor-panel">
      <rect x="895" y="185" width="240" height="243" fill="url(#mint-burst)" role="img" aria-label="Light rays, water drops and mint leaves illustration"/>
      <text class="flavor-top" x="1015" y="305" font-size="36" text-anchor="middle">Fresh Mint</text>
      <text class="flavor-bottom" x="1015" y="348" font-size="42" text-anchor="middle">BLAST</text>
    </g>
  </defs>

  <!-- Top tuck flap -->
  <path class="cut-line" d="M230 45 L290 2 L1075 2 L1135 45 Z"/>

  <!-- Top row -->
  <rect x="230" y="45" width="655" height="140" fill="url(#top-panel-fill)"/>
  <rect x="895" y="45" width="240" height="140" fill="url(#top-side-fill)"/>

  <!-- Row 1: front face + flavor side + end flap -->
  <use href="#front-face"/>
  <use href="#flavor-panel"/>
  <path class="cut-line" d="M1278 185 L1295 185 Q1312 185 1312 205 L1312 408 Q1312 428 1295 428 L1278 428"/>
  <rect x="1135" y="185" width="143" height="243" fill="url(#flap-fill)" role="img" aria-label="Green sparkle rays behind the brand name"/>
  <text class="brand-word" x="1207" y="306" font-size="40" text-anchor="middle" textLength="180" lengthAdjust="spacingAndGlyphs" transform="rotate(-90 1207 306)" dy="14">BRIVANA</text>

  <!-- Row 2: narrow face -->
  <rect x="230" y="428" width="655" height="140" fill="url(#face-fill)"/>
  <ellipse cx="430" cy="500" rx="170" ry="70" fill="url(#logo-glow)" role="img" aria-label="Sparkle burst behind the brand name"/>
  <text class="brand-word" x="330" y="532" font-size="46" textLength="196" lengthAdjust="spacingAndGlyphs">BRIVANA</text>
  <text class="descriptor" x="408" y="552" font-size="11">Fluoride Toothpaste</text>
  <circle class="badge-ring" cx="563" cy="470" r="20"/>
  <text class="badge-number" x="563" y="482" font-size="31" text-anchor="middle">5</text>
  <text class="formula-title" x="590" y="490" font-size="16">ACTION FORMULA</text>
  <g class="benefit-list">
    <circle class="benefit-dot" cx="556" cy="510" r="1.8"/>
    <text class="benefit" x="560" y="514" font-size="11">Protects Against Cavities and Tartar</text>
    <circle class="benefit-dot" cx="556" cy="523" r="1.8"/>
    <text class="benefit" x="560" y="527" font-size="11">Freshens Breath</text>
    <circle class="benefit-dot" cx="556" cy="537" r="1.8"/>
    <text class="benefit" x="560" y="541" font-size="11">Whitens Teeth</text>
    <circle class="benefit-dot" cx="556" cy="550" r="1.8"/>
    <text class="benefit" x="560" y="554" font-size="11">Maintains Healthy Gums</text>
  </g>
  <rect x="895" y="428" width="240" height="140" fill="url(#mint-burst)" role="img" aria-label="Soft light glow with water drops"/>
  <text class="flavor-top" x="1015" y="493" font-size="36" text-anchor="middle">Fresh Mint</text>
  <text class="flavor-bottom" x="1015" y="535" font-size="42" text-anchor="middle">BLAST</text>

  <!-- Row 3: front face repeat + side flaps -->
  <g transform="translate(0 383)">
    <use href="#front-face"/>
    <use href="#flavor-panel"/>
  </g>
  <rect x="117" y="568" width="113" height="242" fill="url(#flap-fill)" role="img" aria-label="Green sparkle rays behind the brand name"/>
  <text class="brand-word" x="173" y="689" font-size="38" text-anchor="middle" textLength="170" lengthAdjust="spacingAndGlyphs" transform="rotate(-90 173 689)" dy="13">BRIVANA</text>
  <rect class="cut-line" x="1135" y="568" width="113" height="242"/>

  <!-- Panel edges and glue stripe -->
  <rect class="glue-stripe" x="884" y="45" width="11" height="765"/>
  <g class="panel-edge">
    <rect x="230" y="45" width="905" height="765"/>
    <line x1="230" y1="185" x2="1135" y2="185"/>
    <line x1="230" y1="428" x2="1135" y2="428"/>
    <line x1="230" y1="568" x2="1135" y2="568"/>
    <rect x="1135" y="185" width="143" height="243"/>
    <rect x="117" y="568" width="113" height="242"/>
  </g>
</svg>
</body>
</html>
```